Webdesign für psychotherapeutische Praxis
Zielgruppe
Psychotherapeutische Praxis für erwachsene Patienten mit psychischen Erkrankungen.
Die Website soll eine solide, vertrauensvolle Information über das therapeutische Angebot bieten sowie alle Informationen zur Erstkontaktaufnahme erhalten.
Aufgabenstellung
Logo füge ich bei. Die Farben, das Design, die Schrift sollen dem Logo entsprechen (Grau, Violett-Pink Töne, moderne Schrift).

```html
<!DOCTYPE html>
<html lang="de">
<head>
<meta charset="utf-8">
<title>Psychotherapeutische Praxis Hollmann</title>
<link href="https://fonts.googleapis.com/css2?family=Fira+Sans:wght@300;400&display=swap" rel="stylesheet">
<style>
:root{
  --violet:#6b5aa8;
  --violet-soft:#7a6bb5;
  --text:#222;
  --nav:#444;
  --white:#fff;
  --band:#6b6a6c;
  --footer:#4a494b;
  --footer-text:#e8e8e8;
}
*{margin:0;padding:0;box-sizing:border-box}
html,body{width:888px;height:1200px;overflow:hidden;background:var(--white)}
body{font-family:"Fira Sans",sans-serif;font-weight:300;color:var(--text);position:relative}
h1,h2,h3{font-weight:300}
.site-header{position:absolute;left:0;top:0;width:888px;height:78px;background:var(--white)}
.brand{position:absolute;left:97px;top:14px;display:flex;align-items:center;gap:24px}
.brand-dot{width:50px;height:50px;border-radius:50%;background:var(--violet-soft)}
.brand-name{color:var(--nav)}
.brand-line{display:block;font-size:11.5px;line-height:15px;font-weight:300}
.brand-line.owner{text-transform:uppercase;font-size:10.5px;font-weight:400;color:#333}
.brand-line.title{font-size:6.2px;line-height:8px;letter-spacing:.2px}
.main-nav a{position:absolute;top:41px;font-size:11px;color:var(--nav);text-decoration:none;font-weight:300}
.hero{position:absolute;left:0;top:78px;width:888px;height:332px;
  background:linear-gradient(100deg,#3f5a32 0%,#6c7b5a 18%,#d7c6c4 32%,#e4d6d3 55%,#8aa6bf 78%,#6f93b4 100%)}
.hero-badge{position:absolute;left:420px;top:163px;width:48px;height:48px;border-radius:50%;background:var(--white)}
.hero-title{position:absolute;left:0;width:888px;top:225px;text-align:center;color:var(--white);font-size:18px;line-height:21px;font-weight:300;text-transform:uppercase}
.hero-button{position:absolute;left:405px;top:281px;width:78px;height:20px;border:1px solid var(--white);color:var(--white);font-size:9.5px;line-height:18px;text-align:center;font-weight:300}
.hero-dots{position:absolute;left:440px;top:357px;display:flex;gap:4px}
.hero-dots span{width:4px;height:4px;border-radius:50%;background:rgba(255,255,255,.5)}
.hero-dots span.active{background:var(--white)}
.notice{position:absolute;left:0;width:888px;top:437px;text-align:center;color:var(--violet);font-size:20px;line-height:24px;font-weight:300}
.welcome{position:absolute;left:102px;top:542px;width:340px;font-size:12px;line-height:15.3px}
.welcome p{margin-bottom:15px}
.welcome .address{padding-left:13px}
.welcome b{font-weight:400;color:#000}
.portrait{position:absolute;left:475px;top:541px;width:337px;height:241px;
  background:linear-gradient(90deg,#cfd3d6 0%,#e6e8ea 40%,#3a3a3c 60%,#dfe2e4 85%,#c8ccd0 100%)}
.caption{position:absolute;left:475px;top:796px;font-size:11.5px;line-height:14px;color:var(--violet-soft)}
.cta-band{position:absolute;left:0;top:895px;width:888px;height:104px;background:var(--band)}
.cta-text{position:absolute;left:258px;top:932px;font-size:21px;color:var(--white);font-weight:300}
.cta-button{position:absolute;left:472px;top:930px;width:135px;height:34px;border:1.5px solid var(--white);color:var(--white);font-size:15px;line-height:31px;text-align:center;font-weight:400}
.site-footer{position:absolute;left:0;top:999px;width:888px;height:201px;background:var(--footer);color:var(--footer-text)}
.footer-col{position:absolute;top:34px}
.footer-col h3{font-size:13.5px;font-weight:400;display:inline-block;padding-bottom:3px;border-bottom:1px solid var(--footer-text);margin-bottom:12px}
.footer-col p{font-size:11.5px;line-height:14px;margin-bottom:11px}
.contact-item{display:flex;align-items:flex-start;gap:8px;font-size:11.5px;line-height:14px;margin-bottom:12px}
.contact-item svg{flex:none;margin-top:1px}
</style>
</head>
<body>
<header class="site-header">
  <div class="brand">
    <div class="brand-dot"></div>
    <div class="brand-name">
      <span class="brand-line">Psychotherapeutische Praxis</span>
      <span class="brand-line owner">Dipl.-Psych. Miriam Hollmann</span>
      <span class="brand-line title">Psychologische Psychotherapeutin (VT)</span>
    </div>
  </div>
  <nav class="main-nav">
    <a style="left:383px">Startseite</a>
    <a style="left:461px">Therapieangebot</a>
    <a style="left:576px">Therapieablauf</a>
    <a style="left:681px">Über mich</a>
    <a style="left:755px">Kontakt</a>
  </nav>
</header>

<section class="hero" role="img" aria-label="Hauseingang der Praxis mit Rosenstrauch und blauen Fensterläden"></section>
<div class="hero-badge"></div>
<h1 class="hero-title">Der Mensch steht im Mittelpunkt<br>unserer ärztlichen Tätigkeit</h1>
<div class="hero-button">Aktuelle Infos</div>
<div class="hero-dots"><span></span><span class="active"></span></div>

<h2 class="notice">Aktuell:&nbsp; Aufgrund der&nbsp; Coronavirus /SARS-CoV-2- Krise<br>biete ich zertifizierte Videosprechstunden an!</h2>

<main class="welcome">
  <p>Liebe Patientinnen, liebe Patienten,</p>
  <p>herzlich willkommen in meiner psychotherapeutischen Praxis</p>
  <p class="address">Lindenweg 12<br>60437 Frankfurt</p>
  <p>Derzeit biete ich die Psychotherapiesitzungen sowohl in der Praxis als auch über <b>Videosprechstunde</b> an.</p>
  <p>Ich nutze einen vom Ärzteverband Mainland <b>zertifizierten Videodienstanbieter</b>, der eine sichere Verbindung zulässt. Sie selbst benötigen lediglich ein Smartphone/ Tablet/ PC und eine stabile Internetverbindung.</p>
  <p>Bitte sprechen Sie mich an, damit wir entscheiden können, welches die beste Lösung derzeit für Sie ist.</p>
  <p>Ihre Psychotherapeutische Praxis</p>
</main>

<div class="portrait" role="img" aria-label="Porträtfoto der Psychotherapeutin in einem hellen Raum"></div>
<div class="caption">Dipl.-Psych. Miriam Hollmann<br>Psychologische Psychotherapeutin<br>Verhaltenstherapie</div>

<section class="cta-band"></section>
<div class="cta-text">Wir sind für Sie da!</div>
<div class="cta-button">Kontakt / Service</div>

<footer class="site-footer">
  <div class="footer-col" style="left:167px">
    <h3>Psychotherapeutische Praxis Hollmann</h3>
    <div class="contact-item">
      <svg width="14" height="20" viewBox="0 0 14 20"><path d="M7 1a6 6 0 0 0-6 6c0 4.5 6 12 6 12s6-7.5 6-12a6 6 0 0 0-6-6z" fill="none" stroke="#e8e8e8" stroke-width="1.4"/><circle cx="7" cy="7" r="2.2" fill="#e8e8e8"/></svg>
      <span>Lindenweg 12<br>60437 Frankfurt/Main</span>
    </div>
    <div class="contact-item">
      <svg width="14" height="14" viewBox="0 0 14 14"><path d="M1 4c3-3 9-3 12 0l-2 2-2-1v-1H5v1L3 6z" fill="#e8e8e8"/><g fill="#e8e8e8"><circle cx="5" cy="8" r=".9"/><circle cx="7" cy="8" r=".9"/><circle cx="9" cy="8" r=".9"/><circle cx="5" cy="10.5" r=".9"/><circle cx="7" cy="10.5" r=".9"/><circle cx="9" cy="10.5" r=".9"/><circle cx="7" cy="13" r=".9"/></g></svg>
      <span>0170 / 555 12 34</span>
    </div>
    <div class="contact-item">
      <svg width="14" height="14" viewBox="0 0 14 14"><path d="M13 1L1 6l5 2 2 5z M6 8l7-7" fill="none" stroke="#e8e8e8" stroke-width="1.2" stroke-linejoin="round"/></svg>
      <span>hollmann-therapie@mailbox.de</span>
    </div>
  </div>
  <div class="footer-col" style="left:454px">
    <h3 style="padding-right:34px">Hinweis</h3>
    <p>Aufgrund der&nbsp; Coronavirus /SARS-CoV-2- Krise<br>biete ich zertifizierte Videosprechstunden an!</p>
    <h3>Telefonische Erreichbarkeit</h3>
    <p>Montags, dienstags, Mittwochs &amp; Donnerstags<br>von 13:00 bis 13:30 Uhr</p>
  </div>
</footer>
</body>
</html>
```